Horizontal scrolling homepage | ||
Consulting company needing a unique layout | ||
Consulting | ||
Qorvinex does consulting and implementation projects within CRM which are the processes around sales, marketing, service, call centers, web shops and more. Even though such engagements of course need the technical involvement from IT, it for sure also needs the business and in this segment the business consists of extrovert colorful people. |
The homepage must be different than the competitors and one way of doing that is by having horizontal scrolling with a menu bar on the left (if the design would be better, you can place it on the top). If it can be done in a cool way, then the left menu bar could be a bit to the right of the left border so that the scrolling background is visible. The scrolling should accelerate and de-accelerate when moving to the part of the homepage that should be displayed. There should not be a scrollbar. Menu: Start (or logo) Packages Services Next Step Career About On the start page there should be a combined sign up for newsletter and contact form (like here: brimtala[dot]dk[slash]om-brimtala). (Title, first name, last name, e-mail, mobile phone number, checkbox for Newsletter sign up and a free text field). The homepage must be easy to extend with additional texts. There should be teasers on the start page that will navigate the user to a place on one of the subpages with more information. It could be interesting to have flipping boxes like in Window Mobile, where one side of the box has a teaser one-liner and when the mouse hovers over it flips and the solution is on the back and when clicked, the page scrolls to the place with more information. But I do not know how easy that will be to implement with HTML5. Inspire me. In addition add the content that normally is part of a start page. You will find logo and teasers as attachments. For additional text use dummy latin. |
Cutting-Edge Unique/Creative Flashy Professional Corporate Modern Elegant Service Oriented |
See logo | ||
Arial Verdana Trebuchet MS |
left side | ||
http://www.morvenquaily.co.uk/ | ||
http://www.pravessa.com/ | ||
http://tunbelfield.com/ | ||
The homepage should be compatible with Internet Explorer and Crome, it should be accessible from Android pads and phones and Apple Iphones and Ipads, but I assume that will all automatically be possible when HTML5 is used for the development. The homepage must be easy to extend with additional menu items / texts. |

```html
<!DOCTYPE html>
<html lang="en">
<head>
<meta charset="utf-8">
<title>Qorvinex – Start</title>
<link href="https://fonts.googleapis.com/css2?family=Arimo:wght@400;700&display=swap" rel="stylesheet">
<style>
  :root {
    --sidebar: #000000;
    --teal-dark: #0d5f70;
    --teal-mid: #12869a;
    --teal-light: #1aa6b8;
    --accent-green: #5f9e1c;
    --menu-start: #1796ad;
    --menu-packages: #7ab51d;
    --menu-services: #8a1f7a;
    --menu-next: #f2a900;
    --menu-career: #1f4fa8;
    --menu-about: #cfcfcf;
    --text: #ffffff;
    --rule: rgba(255,255,255,0.35);
    --input: #ffffff;
    --button: #000000;
  }
  * { box-sizing: border-box; margin: 0; padding: 0; }
  html, body { width: 1200px; height: 686px; overflow: hidden; }
  body {
    position: relative;
    font-family: "Arimo", Arial, sans-serif;
    color: var(--text);
    background: var(--sidebar);
  }
  .sidebar { position: absolute; left: 0; top: 0; width: 276px; height: 686px; background: var(--sidebar); }
  .brand { position: absolute; left: 22px; top: 34px; font-size: 40px; font-weight: 700; color: var(--text); line-height: 1; }
  .main-menu { position: absolute; left: 0; top: 164px; list-style: none; }
  .main-menu li { position: relative; height: 39px; display: flex; align-items: center; font-size: 19px; letter-spacing: 0.5px; }
  .main-menu li::before { content: ""; position: absolute; left: 0; top: 6px; width: 24px; height: 22px; background: var(--bar); }
  .main-menu a { color: var(--text); text-decoration: none; padding-left: 31px; }
  .main-menu .is-active::before { width: 30px; }
  .main-menu .is-active a { padding-left: 67px; }
  .menu-start { --bar: var(--menu-start); }
  .menu-packages { --bar: var(--menu-packages); }
  .menu-services { --bar: var(--menu-services); }
  .menu-next { --bar: var(--menu-next); }
  .menu-career { --bar: var(--menu-career); }
  .menu-about { --bar: var(--menu-about); }

  .stage {
    position: absolute; left: 276px; top: 0; width: 893px; height: 686px;
    background: radial-gradient(ellipse at 55% 75%, var(--teal-light) 0%, var(--teal-mid) 45%, var(--teal-dark) 100%);
  }
  .edge-strip { position: absolute; left: 1169px; top: 0; width: 31px; height: 686px; background: var(--accent-green); }
  .edge-strip::before { content: ""; position: absolute; left: 0; top: 0; width: 24px; height: 40px; background: #e8e8e8; }

  .welcome { position: absolute; left: 53px; top: 42px; width: 430px; }
  .welcome h1 { font-size: 37px; font-weight: 400; margin-bottom: 12px; }
  .welcome p { font-size: 12.5px; line-height: 1.35; margin-bottom: 22px; }

  .divider { position: absolute; left: 514px; top: 34px; width: 1px; height: 630px; background: var(--rule); }

  .contact { position: absolute; left: 545px; top: 56px; width: 320px; font-size: 13px; }
  .contact h2, .teasers h2 { font-size: 15px; font-weight: 400; margin-bottom: 16px; }
  .field { display: flex; align-items: center; height: 24px; }
  .field label { width: 106px; }
  .field input { width: 166px; height: 17px; border: none; background: var(--input); }
  .field-comment { align-items: flex-start; height: 48px; }
  .field-comment textarea { width: 166px; height: 44px; border: none; background: var(--input); resize: none; }
  .newsletter { margin: 4px 0 0 106px; display: flex; align-items: center; gap: 6px; }
  .newsletter input { width: 12px; height: 12px; }
  .form-foot { margin: 6px 0 0 106px; display: flex; align-items: center; gap: 40px; font-size: 9px; }
  .send { background: var(--button); color: var(--text); border: none; font: inherit; font-size: 12px; width: 50px; height: 18px; }

  .band-rule { position: absolute; left: 24px; top: 340px; width: 850px; height: 1px; background: var(--rule); }

  .teasers { position: absolute; top: 358px; }
  .teasers-links { left: 53px; width: 440px; }
  .teasers-links ul { list-style: none; margin-top: 8px; }
  .teasers-links li { display: flex; align-items: center; gap: 12px; height: 31px; font-size: 12px; }
  .teasers-links svg { flex: none; }
  .teasers-links a { color: var(--text); }
  .teasers-info { left: 545px; width: 320px; font-size: 12.5px; line-height: 1.35; }
  .teasers-info p { margin-bottom: 18px; text-align: justify; }
</style>
</head>
<body>
  <aside class="sidebar">
    <div class="brand">Qorvinex</div>
    <ul class="main-menu">
      <li class="menu-start is-active"><a href="#start">START</a></li>
      <li class="menu-packages"><a href="#packages">PACKAGES</a></li>
      <li class="menu-services"><a href="#services">SERVICES</a></li>
      <li class="menu-next"><a href="#next-step">NEXT STEP</a></li>
      <li class="menu-career"><a href="#career">CAREER</a></li>
      <li class="menu-about"><a href="#about">ABOUT</a></li>
    </ul>
  </aside>

  <main class="stage" id="start">
    <section class="welcome">
      <h1>Welcome to Our Site</h1>
      <p>Lorem ipsum dolor sit amet, consectetur adipiscing elit. Nam sit amet justo lectus. Nam tempus vestibulum iaculis. Donec sed odio odio, vitae tristique ante. Maecenas et eros in ante pellentesque sagittis sodales faucibus sapien. Vivamus fringilla dapibus mauris dignissim congue. Nunc rhoncus varius molestie.</p>
      <p>Lorem ipsum dolor sit amet, consectetur adipiscing elit. Nam nec iaculis dui. Nulla facilisi. Suspendisse tincidunt semper lacus ut sodales. Aliquam pulvinar semper ultrices. Maecenas arcu eros, faucibus a varius vel, ornare quis magna. Maecenas faucibus porta semper. Vestibulum pretium fringilla quam sit amet vehicula. Etiam ullamcorper tortor sollicitudin diam facilisis commodo. Sed imperdiet risus sed mi suscipit tincidunt.</p>
    </section>

    <div class="divider"></div>

    <section class="contact">
      <h2>CONTACT US</h2>
      <form>
        <div class="field"><label>First Name*</label><input type="text"></div>
        <div class="field"><label>Last Name*</label><input type="text"></div>
        <div class="field"><label>Mobile*</label><input type="tel"></div>
        <div class="field"><label>Email*</label><input type="email"></div>
        <div class="field field-comment"><label>Comment</label><textarea></textarea></div>
        <div class="newsletter"><input type="checkbox" id="news"><label for="news">News Letter</label></div>
        <div class="form-foot"><span>* Are required</span><button class="send" type="button">Send</button></div>
      </form>
    </section>

    <div class="band-rule"></div>

    <section class="teasers teasers-links">
      <h2>TEASERS</h2>
      <ul>
        <li><svg width="14" height="14" viewBox="0 0 14 14"><circle cx="7" cy="7" r="7" fill="#fff"/><path d="M5 4l4 3-4 3z" fill="#0d5f70"/></svg><a href="#services">Veltrix projects are big and costly, right? – Well, they don't have to be.</a></li>
        <li><svg width="14" height="14" viewBox="0 0 14 14"><circle cx="7" cy="7" r="7" fill="#fff"/><path d="M5 4l4 3-4 3z" fill="#0d5f70"/></svg><a href="#packages">Looking for a system to control your marketing, sale or service processes?</a></li>
        <li><svg width="14" height="14" viewBox="0 0 14 14"><circle cx="7" cy="7" r="7" fill="#fff"/><path d="M5 4l4 3-4 3z" fill="#0d5f70"/></svg><a href="#services">Need something special for your Veltrix implementation?</a></li>
        <li><svg width="14" height="14" viewBox="0 0 14 14"><circle cx="7" cy="7" r="7" fill="#fff"/><path d="M5 4l4 3-4 3z" fill="#0d5f70"/></svg><a href="#about">Relate!</a></li>
        <li><svg width="14" height="14" viewBox="0 0 14 14"><circle cx="7" cy="7" r="7" fill="#fff"/><path d="M5 4l4 3-4 3z" fill="#0d5f70"/></svg><a href="#next-step">How can we help you relate?</a></li>
        <li><svg width="14" height="14" viewBox="0 0 14 14"><circle cx="7" cy="7" r="7" fill="#fff"/><path d="M5 4l4 3-4 3z" fill="#0d5f70"/></svg><a href="#career">Collaborate!</a></li>
      </ul>
    </section>

    <section class="teasers teasers-info">
      <h2>TEASERS</h2>
      <p>Lorem ipsum dolor sit amet, consectetur adipiscing elit. Nam sit amet justo lectus. Nam tempus vestibulum iaculis.</p>
      <p>Donec sed odio odio, vitae tristique ante. Maecenas et eros in ante pellentesque sagittis sodales faucibus sapien.</p>
      <p>Vivamus fringilla dapibus mauris dignissim congue. Nunc rhoncus varius molestie.</p>
    </section>
  </main>

  <div class="edge-strip"></div>
</body>
</html>
```